Our Work

I would like to Upload Pictures and make a flyer showing some of the services we offer. I have attached a sample flyer layout and pictures I would like to use with the services labeled.

```html
<!DOCTYPE html>
<html lang="en">
<head>
<meta charset="utf-8">
<title>Norvell Contracting – Our Services</title>
<link href="https://fonts.googleapis.com/css2?family=Oswald:wght@400;500;600&family=Roboto+Condensed:wght@400&display=swap" rel="stylesheet">
<style>
:root{
  --backdrop:#6f6f6f;
  --paper:#ffffff;
  --blue:#0c2597;
  --yellow:#ffe100;
  --grey:#a7a7a7;
  --ink:#1d1d1d;
}
*{margin:0;padding:0;box-sizing:border-box}
html,body{width:902px;height:1200px;overflow:hidden;background:var(--backdrop)}
.stage{position:absolute;left:0;top:0;width:930px;height:1237px;transform:scale(.9699);transform-origin:0 0}
.flyer{position:absolute;left:67px;top:60px;width:796px;height:1118px;background:var(--paper);overflow:hidden;box-shadow:0 0 14px rgba(0,0,0,.45)}
.shapes{position:absolute;left:0;top:0}
.title{position:absolute;left:0;top:40px;width:100%;text-align:center;color:#fff;font-family:"Oswald",sans-serif;font-weight:500;font-size:78px;line-height:1;letter-spacing:1px}
.brand{position:absolute;left:50px;top:214px;color:var(--blue);font-family:"Oswald",sans-serif;font-weight:500;line-height:1}
.brand .name{display:block;font-size:62px;letter-spacing:6px}
.brand .sub{display:block;font-size:28px;letter-spacing:4px;margin-top:6px}
.photo{position:absolute;width:135px;height:144px;border:3px solid var(--grey)}
.label{position:absolute;font-family:"Oswald",sans-serif;font-weight:400;font-size:10.5px;line-height:15px;color:var(--ink);text-transform:uppercase}
.label.center{text-align:center;transform:translateX(-50%);white-space:nowrap}
.label ul{list-style:none}
.label li{position:relative;padding-left:12px}
.label li::before{content:"";position:absolute;left:1px;top:5px;width:6px;height:6px;border-radius:50%;background:var(--blue)}
.perks{position:absolute;right:76px;top:906px;text-align:right;font-family:"Oswald",sans-serif;font-weight:500;font-size:17.5px;color:var(--blue);line-height:35px}
.perk-icon{position:absolute;width:28px;height:28px;border-radius:50%;background:var(--blue);border:2px solid #fff}
.guaranteed{position:absolute;right:64px;top:1015px;font-family:"Oswald",sans-serif;font-weight:500;font-size:19px;color:var(--blue)}
.badge{position:absolute;left:682px;top:1015px;width:88px;height:88px;border-radius:50%;background:var(--yellow);border:6px solid #1b1b1b}
.contact-head{position:absolute;left:111px;top:1030px;font-family:"Roboto Condensed",sans-serif;font-size:21px;color:#fff}
.contact{position:absolute;top:1068px;display:flex;align-items:center;gap:8px;font-family:"Roboto Condensed",sans-serif;font-size:16px;color:#fff}
.contact svg{flex:none}
</style>
</head>
<body>
<div class="stage">
 <div class="flyer">
  <svg class="shapes" width="796" height="1118" viewBox="0 0 796 1118">
   <polygon points="0,0 796,0 796,134 398,191 0,134" fill="var(--blue)"/>
   <polygon points="0,141 380,188 0,178" fill="var(--yellow)"/>
   <polygon points="796,141 416,188 796,178" fill="var(--yellow)"/>
   <polygon points="0,1030 796,800 796,1118 0,1118" fill="var(--blue)"/>
   <polygon points="206,1016 796,810 796,1020" fill="var(--yellow)"/>
   <g stroke="var(--grey)" stroke-width="3">
    <line x1="136" y1="624" x2="136" y2="530"/>
    <line x1="263" y1="580" x2="263" y2="497"/>
    <line x1="382" y1="540" x2="382" y2="452"/>
    <line x1="561" y1="498" x2="561" y2="394"/>
    <line x1="711" y1="449" x2="711" y2="350"/>
    <line x1="81" y1="670" x2="81" y2="732"/>
    <line x1="216" y1="628" x2="216" y2="689"/>
    <line x1="333" y1="584" x2="333" y2="655"/>
    <line x1="491" y1="493" x2="491" y2="608"/>
    <line x1="619" y1="452" x2="619" y2="534"/>
   </g>
   <polyline points="81,670 136,624 216,628 263,580 333,584 382,540 448,544 491,493 561,498 619,452 711,449" fill="none" stroke="var(--blue)" stroke-width="12" stroke-linejoin="miter"/>
   <g fill="var(--yellow)" stroke="var(--grey)" stroke-width="4">
    <circle cx="81" cy="670" r="15"/><circle cx="136" cy="624" r="15"/><circle cx="216" cy="628" r="15"/>
    <circle cx="263" cy="580" r="15"/><circle cx="333" cy="584" r="15"/><circle cx="382" cy="540" r="15"/>
    <circle cx="491" cy="493" r="15"/><circle cx="561" cy="498" r="15"/><circle cx="619" cy="452" r="15"/>
    <circle cx="711" cy="449" r="15"/>
   </g>
  </svg>

  <h1 class="title">OUR SERVICES</h1>
  <div class="brand"><span class="name">NORVELL</span><span class="sub">CONTRACTING</span></div>

  <div class="photo" style="left:26px;top:386px;background:linear-gradient(160deg,#b98b5e,#7c4f2e)" role="img" aria-label="Interior room under scaffolding being painted"></div>
  <div class="photo" style="left:188px;top:353px;background:linear-gradient(170deg,#a8bdd3,#e8e8ea 60%,#c9c9c9)" role="img" aria-label="Apartment building with balconies under repair"></div>
  <div class="photo" style="left:341px;top:309px;background:linear-gradient(160deg,#f1f1f1,#8a8a8a 70%,#1d3f9a)" role="img" aria-label="Worker repairing a door frame"></div>
  <div class="photo" style="left:490px;top:252px;background:linear-gradient(170deg,#bcd1e6,#e5e2dc 55%,#8d6c5a)" role="img" aria-label="Apartment siding and windows work"></div>
  <div class="photo" style="left:640px;top:204px;background:linear-gradient(170deg,#6f8a52,#b8b2a3 55%,#8d7658)" role="img" aria-label="New concrete steps with wooden forms"></div>
  <div class="photo" style="left:31px;top:732px;background:linear-gradient(160deg,#e6e1d6,#c7c0b2 60%,#2d4a9b)" role="img" aria-label="Workers installing drywall"></div>
  <div class="photo" style="left:180px;top:689px;background:linear-gradient(150deg,#d8d4cc,#6e3f22 55%,#4a2a16)" role="img" aria-label="Hardwood flooring planks"></div>
  <div class="photo" style="left:330px;top:655px;background:linear-gradient(160deg,#9a4a35,#2c3f86 55%,#6b5a48)" role="img" aria-label="Plumber working at a doorway"></div>
  <div class="photo" style="left:483px;top:608px;background:linear-gradient(170deg,#bcd1e6,#e4e2de 55%,#8d6c5a)" role="img" aria-label="Apartment roof repair"></div>
  <div class="photo" style="left:627px;top:534px;background:linear-gradient(170deg,#c6d6e6,#d8d0bf 55%,#6f8a52)" role="img" aria-label="Balcony and deck rehab on apartment building"></div>

  <div class="label center" style="left:131px;top:556px">Exterior &amp; Interior<br>Painting</div>
  <div class="label center" style="left:293px;top:517px">General<br>Carpentry</div>
  <div class="label center" style="left:409px;top:474px">Framing<br>Repairs</div>
  <div class="label" style="left:491px;top:398px">Siding/<br>Gutters/<br>Windows/<br>Doors Concrete</div>
  <div class="label" style="left:633px;top:392px">Concrete<br>Walkways/Stoops</div>
  <div class="label" style="left:52px;top:886px">Drywall Install/<br>Repair Plaster Repairs<br>Wallpaper Removal</div>
  <div class="label" style="left:52px;top:936px">Dryvit/Stucco Repairs</div>
  <div class="label" style="left:193px;top:843px">Flooring/Tile/<br>Carpotillarthrood/<br>Vinyl Leak Investigations:
   <ul><li>Facades</li><li>Roofs</li><li>Interior Leaks</li></ul></div>
  <div class="label" style="left:193px;top:936px">Lead Sale Renovations</div>
  <div class="label center" style="left:381px;top:810px">Plumbing Repairs</div>
  <div class="label center" style="left:545px;top:767px">Roofing Repairs</div>
  <div class="label center" style="left:693px;top:691px">Balcony/Deck Rehab</div>

  <div class="perks">Quick Estimates<br>Yearly Maintenance Contracts<br>Fast Repsonse to General Service Work Order Repairs</div>
  <div class="perk-icon" style="left:736px;top:905px"></div>
  <div class="perk-icon" style="left:736px;top:940px"></div>
  <div class="perk-icon" style="left:736px;top:975px"></div>
  <div class="guaranteed">GUARANTEED!!!</div>
  <div class="badge"></div>

  <div class="contact-head">Contact Us Today!</div>
  <div class="contact" style="left:31px">
   <svg width="18" height="18" viewBox="0 0 18 18"><circle cx="9" cy="9" r="9" fill="var(--yellow)"/><circle cx="9" cy="9" r="5" fill="none" stroke="var(--blue)" stroke-width="1.4"/><line x1="4" y1="9" x2="14" y2="9" stroke="var(--blue)" stroke-width="1.2"/></svg>
   norvellcontracting.com</div>
  <div class="contact" style="left:222px">
   <svg width="18" height="18" viewBox="0 0 18 18"><circle cx="9" cy="9" r="9" fill="var(--yellow)"/><path d="M6 4.5l2 2-1 1.3c.6 1.3 1.6 2.3 2.9 2.9l1.3-1 2 2-1.3 1.6C8.5 13 5 9.5 4.7 6z" fill="var(--blue)"/></svg>
   555.014.0273</div>
  <div class="contact" style="left:367px">
   <svg width="18" height="18" viewBox="0 0 18 18"><circle cx="9" cy="9" r="9" fill="var(--yellow)"/><rect x="4.5" y="6" width="9" height="6.5" fill="var(--blue)"/><path d="M4.5 6l4.5 3.5L13.5 6" fill="none" stroke="var(--yellow)" stroke-width="1"/></svg>
   info@norvellcontracting.com</div>
 </div>
</div>
</body>
</html>
```